Water ATM Card

Need a design for water ATM cards. Size of card is 3.375 x 2.125 inch
On the Front include the Cedar brook Logo.
Bottom right corner should have Price $100
On the Back
This card is to be used to access water refills at any Cedar Brook Water Vending Machines.
Please contact (869) 614 2938 or (869) 731 4072 or email clearflowhq@examplemail.com for any assistance or recharging of card.

```html
<!DOCTYPE html>
<html lang="en">
<head>
<meta charset="utf-8">
<title>Cedar Brook Water Card</title>
<link rel="stylesheet" href="https://fonts.googleapis.com/css2?family=Montserrat:wght@400;700&family=Outfit:wght@300;400;500&display=swap">
<style>
  :root {
    --backdrop: #8fb0d9;
    --brand-blue: #1473bb;
    --brand-green: #3fa34d;
    --ink: #222326;
    --white: #ffffff;
    --rule: #6aa6dc;
  }
  * { box-sizing: border-box; margin: 0; padding: 0; }
  html, body { width: 965px; height: 1200px; overflow: hidden; }
  body { background: var(--backdrop); position: relative; }

  .card {
    position: absolute;
    left: 105px;
    width: 755px;
    height: 475px;
    overflow: hidden;
  }
  .card--front {
    top: 106px;
    background: linear-gradient(180deg, #ffffff 0%, #e9f7fd 38%, #c4ecfb 58%, #6fcaf5 75%, #2f9ff0 90%, #0c72e6 100%);
  }
  .card--back { top: 619px; background: var(--white); }

  .brand {
    position: absolute;
    left: 0; right: 0;
    text-align: center;
    font-family: "Montserrat", sans-serif;
    color: var(--brand-blue);
  }
  .brand__mark {
    position: absolute;
    left: 347px; top: 150px;
    width: 60px; height: 60px;
    border-radius: 50%;
    background: var(--brand-green);
  }
  .brand__name { top: 243px; font-weight: 700; font-size: 46px; letter-spacing: 1px; line-height: 1; }
  .brand__tagline { top: 297px; font-weight: 400; font-size: 29px; line-height: 1; }

  .value {
    position: absolute;
    left: 560px; top: 362px;
    height: 80px;
    border-left: 3px solid var(--white);
    padding-left: 17px;
    color: var(--white);
    font-family: "Outfit", sans-serif;
  }
  .value__amount { display: block; font-size: 60px; font-weight: 500; line-height: 50px; letter-spacing: -1px; margin-top: -2px; }
  .value__label { display: block; font-size: 23px; font-weight: 500; line-height: 1; margin-top: 8px; }

  .usage {
    position: absolute;
    left: 56px; top: 71px;
    font-family: "Outfit", sans-serif;
    font-weight: 300;
    font-size: 29px;
    line-height: 38px;
    color: var(--ink);
    letter-spacing: -0.3px;
  }
  .usage strong { font-weight: 500; }
  .usage-rule {
    position: absolute;
    left: 56px; top: 159px;
    width: 272px; height: 1px;
    background: var(--rule);
  }

  .contact {
    position: absolute;
    left: 56px;
    font-family: "Outfit", sans-serif;
    font-weight: 300;
    font-size: 23px;
    line-height: 29px;
    color: var(--ink);
    display: flex;
    gap: 15px;
  }
  .contact svg { width: 21px; height: 21px; margin-top: 4px; flex: none; fill: var(--brand-blue); }
  .contact--phone { top: 201px; }
  .contact--email { top: 267px; }

  .help-band {
    position: absolute;
    left: 0; top: 350px;
    width: 100%; height: 67px;
    background: var(--brand-blue);
    color: var(--white);
    font-family: "Outfit", sans-serif;
    font-size: 19.5px;
    font-weight: 400;
    line-height: 67px;
    padding-left: 56px;
  }
</style>
</head>
<body>
  <section class="card card--front">
    <span class="brand__mark"></span>
    <h1 class="brand brand__name">CEDAR BROOK</h1>
    <p class="brand brand__tagline">Purified Spring Water</p>
    <div class="value">
      <span class="value__amount">$100</span>
      <span class="value__label">Water Card</span>
    </div>
  </section>

  <section class="card card--back">
    <p class="usage">This card is to be used to access water refills at<br>any <strong>Cedar Brook Water</strong> Vending Machines.</p>
    <div class="usage-rule"></div>

    <div class="contact contact--phone">
      <svg viewBox="0 0 24 24" aria-hidden="true"><path d="M6.6 10.8c1.4 2.8 3.8 5.1 6.6 6.6l2.2-2.2c.3-.3.7-.4 1-.2 1.1.4 2.3.6 3.6.6.6 0 1 .4 1 1V20c0 .6-.4 1-1 1C10.6 21 3 13.4 3 4c0-.6.4-1 1-1h3.5c.6 0 1 .4 1 1 0 1.3.2 2.5.6 3.6.1.3 0 .7-.2 1z"/><path d="M14 3a7 7 0 0 1 7 7h-1.8A5.2 5.2 0 0 0 14 4.8zm0 3.5a3.5 3.5 0 0 1 3.5 3.5h-1.8A1.7 1.7 0 0 0 14 8.3z"/></svg>
      <div>(869) 614 2938<br>(869) 731 4072</div>
    </div>

    <div class="contact contact--email">
      <svg viewBox="0 0 24 24" aria-hidden="true"><path d="M12 2a10 10 0 1 0 0 20 10 10 0 0 0 0-20zm6.9 6h-2.9a15.6 15.6 0 0 0-1.4-3.6A8 8 0 0 1 18.9 8zM12 4c.8 1.2 1.5 2.5 1.9 4h-3.8c.4-1.5 1.1-2.8 1.9-4zM4.3 14a8.2 8.2 0 0 1 0-4h3.4a16.5 16.5 0 0 0 0 4zm.8 2h2.9c.3 1.3.8 2.5 1.4 3.6A8 8 0 0 1 5.1 16zM8 8H5.1a8 8 0 0 1 4.3-3.6C8.8 5.5 8.3 6.7 8 8zm4 12c-.8-1.2-1.5-2.5-1.9-4h3.8c-.4 1.5-1.1 2.8-1.9 4zm2.3-6H9.7a14.7 14.7 0 0 1 0-4h4.6a14.7 14.7 0 0 1 0 4zm.3 5.6c.6-1.1 1.1-2.3 1.4-3.6h2.9a8 8 0 0 1-4.3 3.6zm1.7-5.6a16.5 16.5 0 0 0 0-4h3.4a8.2 8.2 0 0 1 0 4z"/></svg>
      <div>clearflowhq@examplemail.com</div>
    </div>

    <p class="help-band">PLEASE CONTACT FOR ANY ASSISTANCE OR RECHARGING OF CARD.</p>
  </section>
</body>
</html>
```